Business card design and logo for hot water plumbing business

I need a logo and business card for my business which installs hot water heaters
Must have on front:
Brightwell Hot Water Services
Gareth Pemberly
0438617204

Either front or back:
gareth@brightwellhotwaterservices.com.au
ABN 48276053816
Licence No 583420K

On the back in point form:
Supply and installation of
• electric storage
• gas storage/instantaneous
• heat pumps
• solar heaters

Iv provided 3 examples of cards I like but open to different ideas.

```html
<!DOCTYPE html>
<html lang="en">
<head>
<meta charset="utf-8">
<title>Brightwell Hot Water Services – Business Card</title>
<link href="https://fonts.googleapis.com/css2?family=Questrial&display=swap" rel="stylesheet">
<style>
  :root {
    --page-bg: #e9e6e2;
    --card-bg: #ffffff;
    --ink: #222222;
    --band-light: #3a3a3a;
    --band-dark: #1e1e1e;
    --curve-top: #2b2b2b;
    --curve-bottom: #444444;
    --accent-blue: #4a9fe0;
    --white: #ffffff;
  }
  * { margin: 0; padding: 0; box-sizing: border-box; }
  html, body {
    width: 1200px; height: 899px; overflow: hidden;
    background: var(--page-bg);
    font-family: "Questrial", "Century Gothic", sans-serif;
  }
  .card {
    position: absolute;
    width: 669px; height: 382px;
    background: var(--card-bg);
    box-shadow: 0 6px 18px rgba(0,0,0,0.25);
    overflow: hidden;
  }
  .card--front { left: 153px; top: 62px; }
  .card--back  { left: 374px; top: 456px; }

  .brand {
    position: absolute;
    display: flex; align-items: center; gap: 12px;
    color: var(--ink);
    white-space: nowrap;
  }
  .brand__dot {
    border-radius: 50%;
    background: var(--accent-blue);
    flex: none;
  }
  .card--front .brand {
    left: 0; right: 0; top: 150px; justify-content: center;
    font-size: 25px;
  }
  .card--front .brand__dot { width: 34px; height: 34px; }

  .name-band {
    position: absolute; left: 0; right: 0; top: 297px; height: 55px;
    display: flex; color: var(--white);
  }
  .name-band__name {
    flex: 0 0 403px; background: var(--band-light);
    display: flex; align-items: center; padding-left: 92px;
    font-size: 29px;
  }
  .name-band__phone {
    flex: 1; background: var(--band-dark);
    display: flex; align-items: center; padding-left: 42px;
    font-size: 29px; letter-spacing: 0.5px;
  }

  .card--back .brand {
    left: 34px; top: 98px; font-size: 15px; gap: 8px;
  }
  .card--back .brand__dot { width: 18px; height: 18px; }

  .back-curve { position: absolute; inset: 0; width: 100%; height: 100%; }

  .contact {
    position: absolute; left: 249px; top: 116px;
    font-size: 17px; line-height: 22px; color: var(--ink);
  }
  .services {
    position: absolute; left: 42px; top: 226px;
    color: var(--white); font-size: 20px; line-height: 25px;
  }
  .services__title { font-size: 21px; }
  .services__list { list-style: none; }
  .services__list li::before { content: "• "; }
</style>
</head>
<body>
  <section class="card card--front" aria-label="Card front">
    <div class="brand">
      <span class="brand__dot"></span>
      <span class="brand__name">Brightwell Hot Water Services</span>
    </div>
    <div class="name-band">
      <div class="name-band__name">Gareth Pemberly</div>
      <div class="name-band__phone">0438617204</div>
    </div>
  </section>

  <section class="card card--back" aria-label="Card back">
    <svg class="back-curve" viewBox="0 0 669 382" preserveAspectRatio="none" aria-hidden="true">
      <defs>
        <linearGradient id="curveShade" x1="0" y1="0" x2="0" y2="1">
          <stop offset="0" stop-color="#2b2b2b"/>
          <stop offset="1" stop-color="#444444"/>
        </linearGradient>
      </defs>
      <path d="M0 128 C 250 185, 520 245, 669 382 L 0 382 Z" fill="url(#curveShade)"/>
    </svg>
    <div class="brand">
      <span class="brand__dot"></span>
      <span class="brand__name">Brightwell Hot Water Services</span>
    </div>
    <div class="contact">
      <p>gareth@brightwellhotwaterservices.com.au</p>
      <p>ABN 48276053816</p>
      <p>Licence No 583420K</p>
    </div>
    <div class="services">
      <p class="services__title">Supply and installation of</p>
      <ul class="services__list">
        <li>electric storage</li>
        <li>gas storage/instantaneous</li>
        <li>heat pumps</li>
        <li>solar heaters</li>
      </ul>
    </div>
  </section>
</body>
</html>
```